Poster

I need a poster for my business, www.coastaltablejourneysbay.example which some information about the most important activities (Sangria Tasting, Iberian Ham, Charcuteries & Sherry Wine Tasting, Sailboat Experiences and Picnic Experiences). A3 Format. Social media included (@coastaltablejourneyctj), contact information included.

```html
<!DOCTYPE html>
<html lang="en">
<head>
<meta charset="utf-8">
<title>Coastal Table Journeys – Poster</title>
<link href="https://fonts.googleapis.com/css2?family=Bebas+Neue&family=Poppins:wght@400;600;700&family=Yellowtail&family=Kaushan+Script&display=swap" rel="stylesheet">
<style>
:root{
  --maroon:#4a1714;
  --maroon-deep:#3d1211;
  --rust:#8a3a12;
  --amber:#f2a51f;
  --ink:#2a1a18;
  --paper:#ffffff;
  --sea-dark:#5a2a24;
  --sea-light:#c8673a;
}
*{margin:0;padding:0;box-sizing:border-box}
html,body{width:861px;height:1200px;overflow:hidden;background:var(--paper)}
.poster{position:relative;width:861px;height:1200px;background:var(--paper);font-family:'Poppins',sans-serif;color:var(--ink);overflow:hidden}

/* left panel */
.side{position:absolute;left:0;top:0;width:392px;height:1200px;
  background:linear-gradient(180deg,var(--maroon-deep) 0%,var(--maroon) 25%,var(--rust) 60%,#b5541a 80%,var(--sea-dark) 100%)}
.side-edge{position:absolute;left:370px;top:0;height:1200px;width:40px}
.sea-photo{position:absolute;left:0;top:1040px;width:392px;height:160px;
  background:linear-gradient(180deg,#d7783d 0%,#9c4a2c 40%,var(--sea-dark) 100%)}

.brand{position:absolute;left:60px;top:52px;display:flex;align-items:center;gap:14px}
.brand-mark{width:12px;height:12px;background:var(--amber)}
.brand-name{font-family:'Bebas Neue',sans-serif;color:var(--paper);font-size:36px;line-height:32px;letter-spacing:.5px}

.snapshot{position:absolute;width:236px;height:160px;transform:rotate(-8deg);box-shadow:0 3px 8px rgba(0,0,0,.35);border:3px solid var(--paper)}
.tape{position:absolute;width:16px;height:52px;background:var(--amber);transform:rotate(40deg)}
.snap-1{left:72px;top:228px;background:linear-gradient(135deg,#c9b9a8,#6b4a3a 60%,#8a1f25)}
.snap-2{left:72px;top:442px;background:linear-gradient(160deg,#c8c2b8,#3b3530 55%,#1e1b19)}
.snap-3{left:72px;top:656px;background:linear-gradient(180deg,#c9d0d8,#8aa0b8 45%,#1f3f66)}
.snap-4{left:72px;top:876px;background:linear-gradient(160deg,#7a96ad,#c9b7a0 50%,#6c4a30)}

/* right panel */
.headline{position:absolute;left:424px;top:48px}
.enjoy{font-family:'Yellowtail',cursive;color:var(--amber);font-size:64px;line-height:70px;margin-left:8px}
.places{font-family:'Kaushan Script',cursive;color:var(--maroon);font-size:42px;line-height:50px;white-space:nowrap}
.banner{position:absolute;left:378px;top:186px;width:442px;height:50px}
.banner-text{position:absolute;left:410px;top:190px;font-family:'Bebas Neue',sans-serif;font-size:34px;line-height:44px;color:var(--maroon)}

.offer{position:absolute;left:417px;width:420px}
.offer-title{font-family:'Bebas Neue',sans-serif;color:var(--maroon);font-size:22px;line-height:22px;letter-spacing:.2px}
.offer-list{list-style:none;margin-top:14px;width:250px}
.offer-list li{position:relative;padding-left:18px;font-size:10.5px;line-height:12px;margin-bottom:4px}
.offer-list li::before{content:"";position:absolute;left:0;top:3px;width:7px;height:7px;border-radius:50%;background:var(--amber)}
.offer-note{font-weight:700;font-size:10.5px;padding-left:18px;margin-top:6px}

.duration{position:absolute;left:688px;width:76px;text-align:center}
.duration-label{font-family:'Bebas Neue',sans-serif;color:var(--maroon);font-size:22px;line-height:22px}
.duration-box{display:flex;margin-top:2px;height:18px;font-size:12px;line-height:18px}
.duration-box .hr{background:var(--maroon);color:var(--paper);width:30px}
.duration-box .min{background:var(--amber);color:var(--paper);flex:1}

.divider{position:absolute;left:414px;width:352px;height:2px;background:var(--ink);border-radius:1px}

.social{position:absolute;left:432px;top:1036px;display:flex;align-items:center;gap:10px;font-size:16px}
.social-dot{width:14px;height:14px;border-radius:50%;background:var(--amber)}
.site{position:absolute;left:432px;top:1064px;font-size:15.5px;color:var(--maroon)}
.site b{font-weight:700}
</style>
</head>
<body>
<div class="poster">

  <aside class="side">
    <div class="brand">
      <span class="brand-mark"></span>
      <div class="brand-name">Coastal Table<br>Journeys</div>
    </div>

    <div class="snapshot snap-1" role="img" aria-label="Photo of guests tasting red sangria at a seaside table"></div>
    <div class="tape" style="left:104px;top:258px"></div>
    <div class="tape" style="left:326px;top:358px"></div>

    <div class="snapshot snap-2" role="img" aria-label="Photo of olives and Iberian ham bites on a serving board"></div>
    <div class="tape" style="left:104px;top:470px"></div>
    <div class="tape" style="left:326px;top:570px"></div>

    <div class="snapshot snap-3" role="img" aria-label="Photo of a sailboat on the sea at sunset"></div>
    <div class="tape" style="left:104px;top:684px"></div>
    <div class="tape" style="left:326px;top:784px"></div>

    <div class="snapshot snap-4" role="img" aria-label="Photo of a picnic basket with bread, wine and pastries by the shore"></div>
    <div class="tape" style="left:104px;top:878px"></div>
    <div class="tape" style="left:326px;top:1000px"></div>

    <div class="sea-photo" role="img" aria-label="Photo of the sea at sunset"></div>
  </aside>

  <svg class="side-edge" viewBox="0 0 40 1200" preserveAspectRatio="none" aria-hidden="true">
    <path d="M0 0 H22 L18 60 L26 120 L16 200 L24 280 L14 360 L22 440 L16 520 L26 600 L18 680 L24 760 L14 840 L22 920 L18 1000 L26 1080 L20 1200 H0 Z" fill="#f2a51f"/>
    <path d="M0 0 H16 L12 60 L20 120 L10 200 L18 280 L8 360 L16 440 L10 520 L20 600 L12 680 L18 760 L8 840 L16 920 L12 1000 L20 1080 L14 1200 H0 Z" fill="#4a1714"/>
  </svg>

  <header class="headline">
    <div class="enjoy">Enjoy</div>
    <div class="places">Marbella &amp; Estepona</div>
  </header>
  <svg class="banner" viewBox="0 0 442 50" preserveAspectRatio="none" aria-hidden="true">
    <path d="M6 4 L420 0 L410 12 L442 22 L414 30 L430 40 L6 50 L0 30 Z" fill="#f2a51f"/>
  </svg>
  <div class="banner-text">With Coastal Table Journeys</div>

  <section class="offer" style="top:302px">
    <h2 class="offer-title">Sangria Tasting</h2>
    <ul class="offer-list">
      <li>Sampling of 4 types unique &amp; delightful variations of classic Spanish Sangria</li>
      <li>Sherry Wine Sangria, White Wine Sangria, Red Wine Sangria and Rose Cava Sangria</li>
    </ul>
    <p class="offer-note">Light snack of marinated olives &amp; local cheese</p>
  </section>
  <div class="duration" style="top:346px"><div class="duration-label">Duration</div><div class="duration-box"><span class="hr">1h</span><span class="min">30min</span></div></div>

  <div class="divider" style="top:446px"></div>

  <section class="offer" style="top:476px">
    <h2 class="offer-title">Iberian Ham, Charcuteries &amp;<br>Sherry Wine Tasting</h2>
    <ul class="offer-list">
      <li>Tasting of 2 Iberian hams &amp;<br>3 Iberian sausages</li>
      <li>Olives</li>
      <li>Sherry wine</li>
      <li>Detailed explanations of the production processes for Iberian pork products</li>
    </ul>
  </section>
  <div class="duration" style="top:540px"><div class="duration-label">Duration</div><div class="duration-box"><span class="hr">1h</span><span class="min">30min</span></div></div>

  <div class="divider" style="top:640px"></div>

  <section class="offer" style="top:664px">
    <h2 class="offer-title">Sailboat Sangria Tasting Experience</h2>
    <ul class="offer-list">
      <li>Smooth and tranquil sail</li>
      <li>A tasting of artisanal sangrias</li>
      <li>Gourmet appetizers including cheese, iberian saussage, and olives</li>
      <li>Expert guide sharing insights on the history and art of making sangria</li>
      <li>Stunning panoramic views of the Estepona coast</li>
    </ul>
  </section>
  <div class="duration" style="top:722px"><div class="duration-label">Duration</div><div class="duration-box"><span class="hr">1h</span><span class="min">30min</span></div></div>

  <div class="divider" style="top:822px"></div>

  <section class="offer" style="top:848px">
    <h2 class="offer-title">Picnic Brunch Experience</h2>
    <ul class="offer-list">
      <li>Choice of gourmet picnic basket filled with artisanal cheeses, freshly baked bread, cured meats, olives, seasonal fruits, and decadent desserts</li>
      <li>Bottle of premium Spanish wine or refreshing beverages</li>
      <li>Picnic blanket and utensils</li>
      <li>Personalized recommendations for scenic picnic spots in Marbella</li>
    </ul>
  </section>
  <div class="duration" style="top:892px"><div class="duration-label">Duration</div><div class="duration-box"><span class="hr">1h</span><span class="min">30min</span></div></div>

  <div class="social"><span class="social-dot"></span>@coastaltablejourneyctj</div>
  <div class="site">www.<b>coastaltablejourneysbay</b>.example</div>

</div>
</body>
</html>
```